Civic Shieldwell Company

We have design at www.brivatrust.com and want
New site design
Carallax
Images added
Were looking for your eyes. Just placement and look and feel. No hard coding. Design only.

It Company

```html
<!DOCTYPE html>
<html lang="en">
<head>
<meta charset="utf-8">
<title>Brivatrust – Home</title>
<link rel="stylesheet" href="https://fonts.googleapis.com/css2?family=Open+Sans:wght@400;600;700&family=Arimo:wght@700&family=Courier+Prime&display=swap">
<style>
:root{
  --page:#f2f2f2;
  --white:#ffffff;
  --bar-top:#6f9fd2;
  --bar-mid:#3f77b5;
  --bar-bot:#23568f;
  --tab-light:#8fb2db;
  --link:#2f6fb3;
  --text-blue:#2a68aa;
  --tick:#3dbb3d;
  --cross:#c41616;
  --grey-title:#8a8a8a;
  --temp:#f2c64b;
  --sky:#c8c8cc;
}
*{box-sizing:border-box;margin:0;padding:0}
html,body{width:1200px;height:675px;overflow:hidden}
body{background:var(--page);font-family:"Open Sans",sans-serif;position:relative}

.topnav{position:absolute;left:0;top:0;width:1200px;height:40px;
  background:linear-gradient(var(--bar-top),var(--bar-mid) 55%,var(--bar-bot))}
.brand{position:absolute;left:0;top:0;width:112px;height:40px;display:flex;align-items:center;justify-content:center;
  background:linear-gradient(#e6eef8,#b9cde6);color:#1f3f66;font-family:"Courier Prime",monospace;font-size:17px}
.tabs{position:absolute;left:112px;top:0;width:471px;height:40px;background:linear-gradient(#a9c4e4,var(--tab-light) 50%,#6e95c5)}
.tab{position:absolute;top:11px;color:var(--white);font-weight:700;font-size:14px}
.signout{position:absolute;right:0;top:0;width:104px;height:40px;background:linear-gradient(#9cbbe0,#7aa0cf);
  color:var(--white);font-weight:700;font-size:14px;display:flex;align-items:center;justify-content:center}

.panel{position:absolute;background:var(--white)}
.panel-head{height:24px;background:linear-gradient(var(--bar-top),var(--bar-mid) 60%,var(--bar-bot));
  color:var(--white);font-size:10px;font-weight:700;display:flex;align-items:center;justify-content:center;position:relative}
.expand{position:absolute;right:0;top:0;width:30px;height:24px;background:linear-gradient(#8fb2db,#5f8bc2);
  color:var(--white);font-size:18px;font-weight:700;display:flex;align-items:center;justify-content:center}

.main{left:24px;top:71px;width:1154px;height:298px}
.stats{left:24px;top:387px;width:507px;height:267px}
.weather{left:553px;top:387px;width:625px;height:267px}

.item{position:absolute;color:var(--text-blue);font-size:15.5px;line-height:20.5px}
.item h3{font-size:15.5px;font-weight:700}
.item a{color:var(--link)}
.item a.strong{font-weight:700}
.art{position:absolute}
.card-art{left:182px;top:36px;width:101px;height:106px;border-radius:8px;
  background:linear-gradient(135deg,#f2b23a 0 45%,#3aa2e8 45% 100%)}
.bank-name{position:absolute;left:195px;top:206px;width:95px;height:19px;color:var(--text-blue);
  font-weight:700;font-size:14px;display:flex;align-items:center;gap:5px}
.bank-name i{width:10px;height:10px;background:var(--text-blue);display:block}

.stat{position:absolute;color:var(--text-blue);font-size:15.5px;line-height:20.5px}
.stat h3{font-size:15.5px;font-weight:700}
.stat a{color:var(--link)}

.sky{position:absolute;left:0;top:24px;width:625px;height:243px;
  background:radial-gradient(ellipse at 30% 45%,#ffffff 0,#e8e4e4 35%,transparent 60%),
             radial-gradient(ellipse at 80% 55%,#b8b6ba 0,#dcdadc 40%,transparent 70%),
             linear-gradient(#f6f4f4,#ebe9ea)}
.city{position:absolute;left:11px;top:64px;font-family:"Arimo",sans-serif;font-size:62px;color:var(--grey-title)}
.temp{position:absolute;left:453px;top:158px;font-family:"Arimo",sans-serif;font-size:54px;color:var(--temp)}
</style>
</head>
<body>
<header class="topnav">
  <div class="brand">Brivatrust</div>
  <nav class="tabs">
    <span class="tab" style="left:11px">Home</span>
    <span class="tab" style="left:95px">Tab 1</span>
    <span class="tab" style="left:195px">Tab 2</span>
    <span class="tab" style="left:298px">Tab 3</span>
    <span class="tab" style="left:401px">Tab 4</span>
  </nav>
  <div class="signout">Sign Out</div>
</header>

<section class="panel main">
  <div class="panel-head">My Brivatrust<span class="expand">+</span></div>

  <div class="art card-art" role="img" aria-label="Two stacked payment cards"></div>
  <div class="item" style="left:298px;top:72px">
    <h3>My Brivatrust Prepaid Card</h3>
    <p>Balance: £3,198.00</p>
    <p>Text Alerts are on</p>
  </div>

  <svg class="art" style="left:701px;top:56px" width="101" height="73" viewBox="0 0 101 73">
    <defs><linearGradient id="env" x1="0" y1="0" x2="0" y2="1"><stop offset="0" stop-color="#eaf4fc"/><stop offset="1" stop-color="#b9d8f0"/></linearGradient></defs>
    <rect x="3" y="3" width="95" height="67" rx="3" fill="url(#env)" stroke="#1e5fae" stroke-width="5"/>
    <path d="M6 6 L50.5 44 L95 6" fill="none" stroke="#1e5fae" stroke-width="5"/>
    <path d="M6 67 L38 34 M95 67 L63 34" fill="none" stroke="#1e5fae" stroke-width="4"/>
  </svg>
  <div class="item" style="left:808px;top:53px">
    <h3>My E-Mails</h3>
    <p>Protected By Brivatrust</p>
    <p>Last Accessed by 83.192.865.30</p>
  </div>

  <div class="bank-name"><i></i>Northvale</div>
  <div class="item" style="left:299px;top:188px">
    <h3>Recent Transactions From Northvale Card</h3>
    <p>17:39 – £19.00 spent @ Valuemart</p>
    <p>17:39 – £130.00 spent @ Bidhaven</p>
    <p><a class="strong" href="#">Block This Card</a></p>
  </div>

  <svg class="art" style="left:705px;top:162px" width="92" height="92" viewBox="0 0 92 92">
    <g fill="#3cb8ec">
      <rect x="37" y="0" width="18" height="92" rx="3"/>
      <rect x="37" y="0" width="18" height="92" rx="3" transform="rotate(45 46 46)"/>
      <rect x="37" y="0" width="18" height="92" rx="3" transform="rotate(90 46 46)"/>
      <rect x="37" y="0" width="18" height="92" rx="3" transform="rotate(135 46 46)"/>
      <circle cx="46" cy="46" r="34"/>
    </g>
    <circle cx="46" cy="46" r="20" fill="#e6f6fd"/>
  </svg>
  <div class="item" style="left:808px;top:186px">
    <h3>My Settings</h3>
    <p><a href="#">Go to my settings</a></p>
    <p><a href="#">Report Fraud</a></p>
  </div>
</section>

<section class="panel stats">
  <div class="panel-head">Statistics</div>

  <svg class="art" style="left:22px;top:46px" width="57" height="55" viewBox="0 0 57 55"><path d="M3 30 L14 22 L22 36 L47 2 L56 9 L24 53 Z" fill="var(--tick)"/></svg>
  <div class="stat" style="left:98px;top:54px"><h3>My Identity</h3><a href="#">No Problems</a></div>

  <svg class="art" style="left:271px;top:46px" width="58" height="56" viewBox="0 0 58 56"><path d="M4 12 L12 3 L29 19 L46 3 L55 12 L38 28 L55 45 L46 53 L29 37 L12 53 L4 45 L20 28 Z" fill="var(--cross)"/></svg>
  <div class="stat" style="left:343px;top:56px"><h3>My Credit Score</h3><a href="#">Problems Found!</a></div>

  <svg class="art" style="left:22px;top:172px" width="57" height="55" viewBox="0 0 57 55"><path d="M3 30 L14 22 L22 36 L47 2 L56 9 L24 53 Z" fill="var(--tick)"/></svg>
  <div class="stat" style="left:98px;top:179px"><h3>Fraud In My Name</h3><a href="#">No Problems</a></div>

  <svg class="art" style="left:268px;top:172px" width="57" height="55" viewBox="0 0 57 55"><path d="M3 30 L14 22 L22 36 L47 2 L56 9 L24 53 Z" fill="var(--tick)"/></svg>
  <div class="stat" style="left:343px;top:181px"><h3>My Bills</h3><p>No Problems</p></div>
</section>

<section class="panel weather">
  <div class="panel-head">Weather In Aberdeen, UK</div>
  <div class="sky" role="img" aria-label="Soft grey clouds in the sky"></div>
  <div class="city">Aberdeen</div>
  <div class="temp">19.C</div>
</section>
</body>
</html>
```